Building quality affordable homes in Brisbane, Australia for investors and families

We design, build and market our own homes from small single story to large 3 story luxury homes. Our main focus is "duel key" - that is two houses on one lot - a "zooky" (as in where The Zook lived) or attached granny flat.
We have a logo design and need a business card to suit. Something simple but eye catching. We want to communicate: "you are making a smart financial choice buying or building with us".
Unfortunately a lot of information has to be on the card including - Name, position, phone, mobile, fax, email, web address and of course the logo.
Logo in multiple formats and high res now available.

Target Market(s)

Families, contractors, real estate agents, other builders, developers, banks and home buyers.

Industry/Entity Type

Financial

Contact Information for Business Card

Name, position, phone, mobile, fax, email, web address

Font styles to use
Serif

Requirements
Must have
• The logo, and the details.
Nice to have
• Show or explain what we do - design, build and market affordable homes.
Should not have
• Nothing too fancy, outrageous - building companies are normally very straight.

```html
<!DOCTYPE html>
<html lang="en">
<head>
<meta charset="utf-8">
<title>Brightlot Homes – Business Card</title>
<link href="https://fonts.googleapis.com/css2?family=Open+Sans:wght@400;600;700&display=swap" rel="stylesheet">
<style>
  :root {
    --brand-blue: #0b63c9;
    --brand-blue-light: #7eaade;
    --card-black: #1f1f1f;
    --card-white: #ffffff;
    --text-light: #f2f2f2;
    --text-muted: #d0d0d0;
    --stage: #e7e4e1;
  }
  * { margin: 0; padding: 0; box-sizing: border-box; }
  html, body {
    width: 1200px; height: 960px; overflow: hidden;
    background: var(--stage);
    font-family: "Open Sans", sans-serif;
  }
  .stage {
    width: 1200px; height: 960px;
    display: flex; flex-direction: column; align-items: center; justify-content: center;
    gap: 50px;
  }
  .card {
    width: 700px; height: 400px; border-radius: 20px; overflow: hidden; position: relative;
    box-shadow: 0 10px 24px rgba(0,0,0,0.18);
  }
  /* Back side */
  .card-back {
    background: var(--brand-blue);
    display: flex; flex-direction: column; align-items: center; justify-content: center;
    color: var(--card-white);
  }
  .back-mark { display: flex; align-items: center; gap: 16px; }
  .back-mark .mark-square { width: 64px; height: 64px; background: var(--card-white); }
  .back-mark .mark-name { font-size: 44px; font-weight: 700; color: var(--card-white); }
  .back-web { margin-top: 26px; font-size: 17px; letter-spacing: 0.3px; }

  /* Front side */
  .card-front { background: var(--card-black); }
  .front-top {
    position: absolute; left: 0; top: 0; width: 100%; height: 160px;
    background: var(--card-white);
    display: flex; align-items: center; padding-left: 44px; gap: 18px;
  }
  .front-stripe {
    position: absolute; left: 0; top: 160px; width: 100%; height: 12px;
    background: var(--brand-blue);
  }
  .brand-square { width: 84px; height: 84px; background: var(--brand-blue-light); }
  .brand-text { display: flex; flex-direction: column; }
  .brand-name { font-size: 54px; font-weight: 700; color: var(--brand-blue); line-height: 1; }
  .brand-sub { font-size: 15px; font-weight: 600; color: var(--card-black); letter-spacing: 1px; margin-top: 6px; }

  .person { position: absolute; left: 44px; top: 200px; color: var(--text-light); }
  .person-name { font-size: 30px; font-weight: 700; }
  .person-role { font-size: 15px; color: var(--text-muted); margin-top: -2px; }

  .contacts {
    position: absolute; left: 44px; top: 278px; list-style: none;
    color: var(--text-light); font-size: 17px;
  }
  .contacts li { display: flex; align-items: center; gap: 14px; height: 27px; }
  .contacts svg { width: 18px; height: 18px; fill: var(--text-light); flex: none; }
</style>
</head>
<body>
<main class="stage">
  <section class="card card-back" aria-label="Business card back">
    <div class="back-mark">
      <span class="mark-square"></span>
      <span class="mark-name">Brightlot</span>
    </div>
    <p class="back-web">www.brightlothomes.au</p>
  </section>

  <section class="card card-front" aria-label="Business card front">
    <div class="front-top">
      <span class="brand-square"></span>
      <div class="brand-text">
        <span class="brand-name">Brightlot</span>
        <span class="brand-sub">HOMES COMPANY PTY LTD</span>
      </div>
    </div>
    <div class="front-stripe"></div>

    <div class="person">
      <p class="person-name">Jonathan Doe</p>
      <p class="person-role">Managing Director</p>
    </div>

    <ul class="contacts">
      <li>
        <svg viewBox="0 0 20 20"><circle cx="10" cy="6" r="4.5"/><path d="M2 19c0-5 3.5-7.5 8-7.5s8 2.5 8 7.5z"/></svg>
        <span>07 3184 2265</span>
      </li>
      <li>
        <svg viewBox="0 0 20 20"><path d="M5 2l3 4-2 2c1 2.5 3.5 5 6 6l2-2 4 3-2 3C9 18 2 11 2 4z"/></svg>
        <span>0412 658 903</span>
      </li>
      <li>
        <svg viewBox="0 0 20 20"><rect x="5" y="2" width="10" height="5"/><rect x="2" y="8" width="16" height="8" rx="1"/><rect x="5" y="13" width="10" height="5" fill="#1f1f1f" stroke="#f2f2f2" stroke-width="1.5"/></svg>
        <span>07 3184 2299</span>
      </li>
      <li>
        <svg viewBox="0 0 20 20"><rect x="1" y="4" width="18" height="12" fill="none" stroke="#f2f2f2" stroke-width="2"/><path d="M1 4l9 7 9-7" fill="none" stroke="#f2f2f2" stroke-width="2"/></svg>
        <span>hello@brightlothomes.au</span>
      </li>
    </ul>
  </section>
</main>
</body>
</html>
```